Car wash line needed for the pylon inscription

We need a design template / print template for our advertising pylon so that the Plavex plates can be printed. The area to be printed is approx. 1.5m wide and approx. 2.70m high. We operate a car wash about 30m long. The washing rollers are equipped with scratch-free Nerva Plush foam material. Before the vehicle is put into the car wash it gets a manual high pressure pre-wash. There are four different washing programs: basic laundry € 7.50 (wheel cleaning, intensive washing, gloss drying comfort care € 10.50 (like base + active foam) special care € 13.00 (like comfort + glossy sealing with lotus wax) premium care € 15.50 (like special care + Underbody wash) The pylon is right on the driveway on a busy road, we want to achieve maximum attention with the pylons. It should not be too much content because the vehicles drive past it, due to an immediate gyro, the speed is however at about 40Km / h. Opening hours Mon-Fri. 08: 00-19: 00 Sat 07: 00-19: 00 The Plavex plates are red. The enclosed files show our pylon with a little appealing design proposal our advertising agency and the real local places. For the opinion you can see on the following link a clipvane video with a comparable car wash like ours, the washing process is well illustrated there. https://www.clipvane.net/watch?v=Rk4LmQw9ZpT Furthermore, we have a bonus card system who has washed our car 10 times gets the 11 laundry for free. From foam additives we use active foam from the comfort care and from the special care gets the vehicle lotus wax, which has the effect that the paint is sealed and keeps the shine longer. We need a design template / print template for our advertising pylon so that the Plavex plates can be printed. The area to be printed is approx. 1.5m wide and approx. 2.70m high. We operate a car wash about 30m long. The washing rollers are equipped with scratch-free Nerva Plush foam material. Before the vehicle is put into the car wash it gets a manual high pressure pre-wash. There are four different washing programs: basic laundry € 7.50 (wheel cleaning, intensive washing, gloss drying comfort care € 10.50 (like base + active foam) special care € 13.00 (like comfort + glossy sealing with lotus wax) premium care € 15.50 (like special care + Underbody wash) The pylon is right on the driveway on a busy road, we want to achieve maximum attention with the pylons. It should not be too much content because the vehicles drive past it, due to an immediate gyro, the speed is however at about 40Km / h. Opening hours Mon-Fri. 08: 00-19: 00 Sat 07: 00-19: 00 The Plavex plates are red. The enclosed files show our pylon with a little appealing design proposal our advertising agency and the real local places. For the opinion you can see on the following link a clipvane video with a comparable car wash like ours, the washing process is well illustrated there. https://www.clipvane.net/watch?v=Rk4LmQw9ZpT Furthermore, we have a bonus card system who has washed our car 10 times gets the 11 laundry for free. From foam additives we use active foam from the comfort care and from the special care gets the vehicle lotus wax, which has the effect that the paint is sealed and keeps the shine longer. We need a design template / print template for our advertising pylon so that the Plavex plates can be printed. The area to be printed is approx. 1.5m wide and approx. 2.70m high. We operate a car wash about 30m long. The washing rollers are equipped with scratch-free Nerva Plush foam material. Before the vehicle is put into the car wash it gets a manual high pressure pre-wash. There are four different washing programs: basic laundry € 7.50 (wheel cleaning, intensive washing, gloss drying comfort care € 10.50 (like base + active foam) special care € 13.00 (like comfort + glossy sealing with lotus wax) premium care € 15.50 (like special care + Underbody wash) The pylon is right on the driveway on a busy road, we want to achieve maximum attention with the pylons. It should not be too much content because the vehicles drive past it, due to an immediate gyro, the speed is however at about 40Km / h. Opening hours Mon-Fri. 08: 00-19: 00 Sat 07: 00-19: 00 The Plavex plates are red. The enclosed files show our pylon with a little appealing design proposal our advertising agency and the real local places. For the opinion you can see on the following link a clipvane video with a comparable car wash like ours, the washing process is well illustrated there. https://www.clipvane.net/watch?v=Rk4LmQw9ZpT Furthermore, we have a bonus card system who has washed our car 10 times gets the 11 laundry for free. From foam additives we use active foam from the comfort care and from the special care gets the vehicle lotus wax, which has the effect that the paint is sealed and keeps the shine longer. We need a design template / print template for our advertising pylon so that the Plavex plates can be printed. The area to be printed is approx. 1.5m wide and approx. 2.70m high. We operate a car wash about 30m long. The washing rollers are equipped with scratch-free Nerva Plush foam material. Before the vehicle is put into the car wash it gets a manual high pressure pre-wash. There are four different washing programs: basic laundry € 7.50 (wheel cleaning, intensive washing, gloss drying comfort care € 10.50 (like base + active foam) special care € 13.00 (like comfort + glossy sealing with lotus wax) premium care € 15.50 (like special care + Underbody wash) The pylon is right on the driveway on a busy road, we want to achieve maximum attention with the pylons. It should not be too much content because the vehicles drive past it, due to an immediate gyro, the speed is however at about 40Km / h. Opening hours Mon-Fri. 08: 00-19: 00 Sat 07: 00-19: 00 The Plavex plates are red. The enclosed files show our pylon with a little appealing design proposal our advertising agency and the real local places. For the opinion you can see on the following link a clipvane video with a comparable car wash like ours, the washing process is well illustrated there. https://www.clipvane.net/watch?v=Rk4LmQw9ZpT Furthermore, we have a bonus card system who has washed our car 10 times gets the 11 laundry for free. From foam additives we use active foam from the comfort care and from the special care gets the vehicle lotus wax, which has the effect that the paint is sealed and keeps the shine longer. We need a design template / print template for our advertising pylon so that the Plavex plates can be printed. The area to be printed is approx. 1.5m wide and approx. 2.70m high. We operate a car wash about 30m long. The washing rollers are equipped with scratch-free Nerva Plush foam material. Before the vehicle is put into the car wash it gets a manual high pressure pre-wash. There are four different washing programs: basic laundry € 7.50 (wheel cleaning, intensive washing, gloss drying comfort care € 10.50 (like base + active foam) special care € 13.00 (like comfort + glossy sealing with lotus wax) premium care € 15.50 (like special care + Underbody wash) The pylon is right on the driveway on a busy road, we want to achieve maximum attention with the pylons. It should not be too much content because the vehicles drive past it, due to an immediate gyro, the speed is however at about 40Km / h. Opening hours Mon-Fri. 08: 00-19: 00 Sat 07: 00-19: 00 The Plavex plates are red. The enclosed files show our pylon with a little appealing design proposal our advertising agency and the real local places. For the opinion you can see on the following link a clipvane video with a comparable car wash like ours, the washing process is well illustrated there. https://www.clipvane.net/watch?v=Rk4LmQw9ZpT Furthermore, we have a bonus card system who has washed our car 10 times gets the 11 laundry for free. From foam additives we use active foam from the comfort care and from the special care gets the vehicle lotus wax, which has the effect that the paint is sealed and keeps the shine longer. We need a design template / print template for our advertising pylon so that the Plavex plates can be printed. The area to be printed is approx. 1.5m wide and approx. 2.70m high. We operate a car wash about 30m long. The washing rollers are equipped with scratch-free Nerva Plush foam material. Before the vehicle is put into the car wash it gets a manual high pressure pre-wash. There are four different washing programs: basic laundry € 7.50 (wheel cleaning, intensive washing, gloss drying comfort care € 10.50 (like base + active foam) special care € 13.00 (like comfort + glossy sealing with lotus wax) premium care € 15.50 (like special care + Underbody wash) The pylon is right on the driveway on a busy road, we want to achieve maximum attention with the pylons. It should not be too much content because the vehicles drive past it, due to an immediate gyro, the speed is however at about 40Km / h. Opening hours Mon-Fri. 08: 00-19: 00 Sat 07: 00-19: 00 The Plavex plates are red. The enclosed files show our pylon with a little appealing design proposal our advertising agency and the real local places. For the opinion you can see on the following link a clipvane video with a comparable car wash like ours, the washing process is well illustrated there. https://www.clipvane.net/watch?v=Rk4LmQw9ZpT Furthermore, we have a bonus card system who has washed our car 10 times gets the 11 laundry for free. From foam additives we use active foam from the comfort care and from the special care gets the vehicle lotus wax, which has the effect that the paint is sealed and keeps the shine longer. We need a design template / print template for our advertising pylon so that the Plavex plates can be printed. The area to be printed is approx. 1.5m wide and approx. 2.70m high. We operate a car wash about 30m long. The washing rollers are equipped with scratch-free Nerva Plush foam material. Before the vehicle is put into the car wash it gets a manual high pressure pre-wash. There are four different washing programs: basic laundry € 7.50 (wheel cleaning, intensive washing, gloss drying comfort care € 10.50 (like base + active foam) special care € 13.00 (like comfort + glossy sealing with lotus wax) premium care € 15.50 (like special care + Underbody wash) The pylon is right on the driveway on a busy road, we want to achieve maximum attention with the pylons. It should not be too much content because the vehicles drive past it, due to an immediate gyro, the speed is however at about 40Km / h. Opening hours Mon-Fri. 08: 00-19: 00 Sat 07: 00-19: 00 The Plavex plates are red. The enclosed files show our pylon with a little appealing design proposal our advertising agency and the real local places. For the opinion you can see on the following link a clipvane video with a comparable car wash like ours, the washing process is well illustrated there. https://www.clipvane.net/watch?v=Rk4LmQw9ZpT Furthermore, we have a bonus card system who has washed our car 10 times gets the 11 laundry for free. From foam additives we use active foam from the comfort care and from the special care gets the vehicle lotus wax, which has the effect that the paint is sealed and keeps the shine longer. We need a design template / print template for our advertising pylon so that the Plavex plates can be printed. The area to be printed is approx. 1.5m wide and approx. 2.70m high. We operate a car wash about 30m long. The washing rollers are equipped with scratch-free Nerva Plush foam material. Before the vehicle is put into the car wash it gets a manual high pressure pre-wash. There are four different washing programs: basic laundry € 7.50 (wheel cleaning, intensive washing, gloss drying comfort care € 10.50 (like base + active foam) special care € 13.00 (like comfort + glossy sealing with lotus wax) premium care € 15.50 (like special care + Underbody wash) The pylon is right on the driveway on a busy road, we want to achieve maximum attention with the pylons. It should not be too much content because the vehicles drive past it, due to an immediate gyro, the speed is however at about 40Km / h. Opening hours Mon-Fri. 08: 00-19: 00 Sat 07: 00-19: 00 The Plavex plates are red. The enclosed files show our pylon with a little appealing design proposal our advertising agency and the real local places. For the opinion you can see on the following link a clipvane video with a comparable car wash like ours, the washing process is well illustrated there. https://www.clipvane.net/watch?v=Rk4LmQw9ZpT Furthermore, we have a bonus card system who has washed our car 10 times gets the 11 laundry for free. From foam additives we use active foam from the comfort care and from the special care gets the vehicle lotus wax, which has the effect that the paint is sealed and keeps the shine longer. We need a design template / print template for our advertising pylon so that the Plavex plates can be printed. The area to be printed is approx. 1.5m wide and approx. 2.70m high. We operate a car wash about 30m long. The washing rollers are equipped with scratch-free Nerva Plush foam material. Before the vehicle is put into the car wash it gets a manual high pressure pre-wash. There are four different washing programs: basic laundry € 7.50 (wheel cleaning, intensive washing, gloss drying comfort care € 10.50 (like base + active foam) special care € 13.00 (like comfort + glossy sealing with lotus wax) premium care € 15.50 (like special care + Underbody wash) The pylon is right on the driveway on a busy road, we want to achieve maximum attention with the pylons. It should not be too much content because the vehicles drive past it, due to an immediate gyro, the speed is however at about 40Km / h. Opening hours Mon-Fri. 08: 00-19: 00 Sat 07: 00-19: 00 The Plavex plates are red. The enclosed files show our pylon with a little appealing design proposal our advertising agency and the real local places. For the opinion you can see on the following link a clipvane video with a comparable car wash like ours, the washing process is well illustrated there. https://www.clipvane.net/watch?v=Rk4LmQw9ZpT Furthermore, we have a bonus card system who has washed our car 10 times gets the 11 laundry for free. From foam additives we use active foam from the comfort care and from the special care gets the vehicle lotus wax, which has the effect that the paint is sealed and keeps the shine longer.

Target Market(s)

germany

Colors

Designer to choose colors to be used in the design.

Requirements
Must have
• Print template for the print job in the accepted formats. Of course, the design must be in German
Nice to have
• Colors that attract attention, but are still serious. The content must be perceived when passing by and the customers must be aware of the car wash.
Should not have
• Kitschiges Design Too much content which takes longer to be read.

```html
<!DOCTYPE html>
<html lang="de">
<head>
<meta charset="utf-8">
<title>Pylon – Nerva Plush Schaumstoffwalzen</title>
<link rel="stylesheet" href="https://fonts.googleapis.com/css2?family=Fira+Sans+Condensed:wght@700;800&display=swap">
<style>
  :root {
    --page: #ffffff;
    --pylon-red: #ff0000;
    --white: #ffffff;
    --ink: #000000;
    --accent-blue: #00a6ec;
  }
  html, body {
    margin: 0;
    padding: 0;
    width: 1200px;
    height: 1000px;
    overflow: hidden;
    background: var(--page);
  }
  .canvas {
    position: relative;
    width: 1200px;
    height: 1000px;
    font-family: "Fira Sans Condensed", "Arial Narrow", sans-serif;
    font-weight: 700;
  }
  .pylon {
    position: absolute;
    left: 293px;
    top: 31px;
    width: 612px;
    height: 938px;
    background: var(--pylon-red);
  }
  .headline {
    position: absolute;
    left: 355px;
    margin: 0;
    color: var(--white);
    text-transform: uppercase;
    line-height: 1;
    white-space: nowrap;
  }
  .headline--intro { top: 106px; font-size: 54px; }
  .headline--product { top: 180px; font-size: 80px; }
  .headline--rollers { top: 275px; font-size: 51px; }
  .offer {
    position: absolute;
    left: 0;
    top: 0;
  }
  .offer text {
    font-family: "Fira Sans Condensed", "Arial Narrow", sans-serif;
    font-weight: 700;
    text-anchor: middle;
  }
  .hours {
    position: absolute;
    left: 293px;
    width: 612px;
    top: 902px;
    margin: 0;
    text-align: center;
    color: var(--white);
    font-size: 26px;
    line-height: 1;
    white-space: nowrap;
  }
</style>
</head>
<body>
<main class="canvas">
  <section class="pylon" aria-label="Werbepylon Autowaschanlage"></section>

  <h1 class="headline headline--intro">Lackschonend mit</h1>
  <p class="headline headline--product">Nerva Plush</p>
  <p class="headline headline--rollers">Schaumstoffwalzen</p>

  <svg class="offer" width="1200" height="1000" viewBox="0 0 1200 1000" aria-label="Angebot Waschgutscheine">
    <polygon class="offer__tick" fill="var(--white)"
      points="397,517 541,660 801,401 801,575 541,835 397,690"/>
    <text fill="var(--white)" font-size="38" transform="translate(487,572) rotate(45)">NUR HIER!</text>
    <text fill="var(--accent-blue)" font-size="36" transform="translate(527,694) rotate(45)">WASCH</text>
    <text fill="var(--accent-blue)" font-size="36" transform="translate(494,727) rotate(45)">GUTSCHEINE!</text>
    <text fill="var(--ink)" font-size="40" transform="translate(674,596) rotate(-45)">SPAREN SIE 10%</text>
    <text fill="var(--accent-blue)" font-size="40" transform="translate(712,631) rotate(-45)">FÜR 10X</text>
  </svg>

  <p class="hours">MON-FRI. 08:00-19:00 | SAT 07:00-19:00</p>
</main>
</body>
</html>
```